The Radiant Scroll of Petitions, Steadfast Petitions Across Seasons of Trial

I want a book cover design, The book is a prayer book. Pleas no design with only words. I want something creative and original. Something that attracts attention just by looking at the cover. Something powerful. This book is for people that are experiencing issues and need prayer. This book is also for those that want to pray and pray effectively. Not only will there be prayers. But they will learn the dynamics of prayer and how to pray effectively and from the right position. This book is filled with power yet effective prayers that will.have the ability to break bondages off people lives.
Below is some book covers that I found. I posted them to give an idea of what im looking for. Something that catches the attention of a reader.

Target Market(s)

Everyone, religious people

Industry/Entity Type

Religious

Font styles to use
Serif
Sans Serif

Requirements
Must have
• Creativity, originality,
Nice to have
• Professional looking. Powerful looking
Should not have
• Should not have just one color with big ole words across the whole book.

```html
<!DOCTYPE html>
<html lang="en">
<head>
<meta charset="utf-8">
<title>The Radiant Scroll of Petitions – Cover Wrap</title>
<link rel="stylesheet" href="https://fonts.googleapis.com/css2?family=Anton&family=Crimson+Text:wght@400&family=Archivo+Black&display=swap">
<style>
  :root {
    --stage: #c9d2d3;
    --cover-dark: #100e0d;
    --cover-brown: #3e2a1d;
    --glow-gold: #d99a3a;
    --glow-amber: #7a4e1e;
    --ember: #5a2416;
    --ink-light: #ffffff;
    --ink-body: #e9e4dc;
  }
  * { box-sizing: border-box; margin: 0; padding: 0; }
  html, body { width: 1200px; height: 800px; overflow: hidden; }
  body { background: var(--stage); position: relative; }

  .front-cover {
    position: absolute; left: 200px; top: 110px; width: 360px; height: 560px;
    background: var(--cover-dark); overflow: hidden;
  }
  .front-cover__photo {
    position: absolute; inset: 0;
    background:
      radial-gradient(circle at 58% 36%, var(--glow-gold) 0%, rgba(170,105,40,0.65) 22%, rgba(90,55,25,0.35) 42%, transparent 62%),
      linear-gradient(180deg, var(--cover-brown) 0%, #2a1c14 44%, var(--ember) 51%, #1c1412 58%, var(--cover-dark) 100%);
  }
  .front-cover__title {
    position: absolute; left: 0; right: 0; top: 246px;
    font-family: "Anton", sans-serif; font-weight: 400; color: var(--ink-light);
    text-align: center; text-transform: uppercase; line-height: 0.95;
  }
  .front-cover__title span { display: block; }
  .front-cover__title .title-the { font-size: 40px; }
  .front-cover__title .title-main { font-size: 56px; }
  .front-cover__title .title-small { display: inline; font-size: 32px; }
  .front-cover__subtitle {
    position: absolute; left: 30px; right: 30px; top: 452px;
    font-family: "Crimson Text", serif; font-size: 20px; line-height: 1.05;
    color: var(--ink-light); text-align: center;
  }

  .back-cover {
    position: absolute; left: 595px; top: 110px; width: 330px; height: 560px;
    background: linear-gradient(180deg, #2b2b2b 0%, var(--cover-dark) 16%, var(--cover-dark) 100%);
    overflow: hidden;
  }
  .back-cover__bokeh {
    position: absolute; left: 60px; right: 0; bottom: 0; height: 220px;
    background:
      radial-gradient(circle at 30% 60%, rgba(120,70,30,0.3) 0%, transparent 40%),
      radial-gradient(circle at 85% 30%, rgba(140,80,30,0.25) 0%, transparent 35%),
      radial-gradient(circle at 60% 85%, rgba(90,50,25,0.3) 0%, transparent 45%);
  }
  .back-cover__copy {
    position: absolute; left: 4px; right: 46px; top: 58px;
    font-family: "Crimson Text", serif; font-size: 11.5px; line-height: 1.08;
    color: var(--ink-body); text-align: justify;
  }
  .back-cover__copy p + p { margin-top: 14px; }
  .back-cover__copy p.gap { margin-top: 44px; }

  .spine {
    position: absolute; left: 925px; top: 110px; width: 30px; height: 560px;
    background: var(--cover-dark); border-left: 1px solid #222;
  }
  .spine__text {
    position: absolute; left: 50%; top: 36px;
    transform: translateX(-50%); writing-mode: vertical-rl;
    color: var(--ink-light); white-space: nowrap; line-height: 1.05;
  }
  .spine__title { font-family: "Archivo Black", sans-serif; font-size: 12px; letter-spacing: 0.04em; text-transform: uppercase; }
  .spine__subtitle { font-family: "Crimson Text", serif; font-size: 9.5px; }
</style>
</head>
<body>
  <section class="front-cover">
    <div class="front-cover__photo" role="img" aria-label="Photograph of a lit candle on the left with warm golden light glowing above, fading to dark"></div>
    <h1 class="front-cover__title">
      <span class="title-the">The</span>
      <span class="title-main">Radiant</span>
      <span class="title-main">Scroll <span class="title-small">of</span></span>
      <span class="title-main">Petitions</span>
    </h1>
    <p class="front-cover__subtitle">Steadfast Petitions Across<br>Seasons of Trial</p>
  </section>

  <section class="back-cover">
    <div class="back-cover__bokeh" role="img" aria-label="Soft out-of-focus amber light circles"></div>
    <div class="back-cover__copy">
      <p>I want a book cover design, The book is a prayer book. Pleas no design with only words. I want something creative and original. Something that attracts attention just by looking at the cover. Something powerful. This book is for people that are experiencing issues and need prayer. This book is also for those that want to pray and pray effectively. Not only will there be prayers. But they will learn the dynamics of prayer and how to pray effectively and from the right position. This book is filled with power yet effective prayers that will.have the ability to break bondages off people lives. &lt;br/&gt;Below is some book covers that I found. I posted them to give an idea of what im looking for. Something that catches the attention of a reader.</p>
      <p>I want a book cover design, The book is a prayer book. Pleas no design with only words. I want something creative and original. Something that attracts attention just by looking at the cover. Something powerful. This book is for people that are experiencing issues and need prayer. This book is also for those that want to pray and pray effectively. Not only will there be prayers. But they will learn the dynamics of prayer and how to pray effectively and from the right position. This book is filled with power yet effective prayers that</p>
      <p class="gap">I want a book cover design, The book is a prayer book. Pleas no design with only words. I want something creative and original. Something that attracts attention just by looking at the cover. Something powerful. This book is for people that are experiencing issues and need prayer. This book is also for those that want to pray and pray effectively. Not only will there be prayers. But they will learn the dynamics of prayer and how to pray effectively and from the right position. This book is filled with power yet effective prayers that</p>
    </div>
  </section>

  <aside class="spine">
    <div class="spine__text">
      <div class="spine__title">The Radiant Scroll of Petitions</div>
      <div class="spine__subtitle">Steadfast Petitions Across Seasons of Trial</div>
    </div>
  </aside>
</body>
</html>
```